Website Refresh Needed - Large Couples Therapy Group

We are a large couples counselling group in Australia, and we have some key pages of our website that need refreshing, as it's a few years old now.
Similar colour palette as currently, and the same colours as the logo. No new logo required.
Total of 7 new (updated) page templates designs are needed:
1. HOME: https://www.velmoraclinic.com.au/
2: CONTACT US: https://www.velmoraclinic.com.au/contact/
3: RC CITY PAGE: https://www.velmoraclinic.com.au/city/sydney/
4: ST CITY PAGE: https://www.velmoraclinic.com.au/our-counselling/sex-therapy/sex-therapy-sydney/
5: ALL BLOGS: https://www.velmoraclinic.com.au/blog/
6: BLOG: https://www.velmoraclinic.com.au/sexual-desires-in-men-and-women-what-are-the-real-differences/
7: MAIN STANDARD PAGE: https://www.velmoraclinic.com.au/our-counselling/couples-relationship-counselling/

Target Market(s)

couples who are going through a crisis in their relationship or marriage.

Number of Pages Required

5+ page

Colors
86cfc6
b8a6cd
cfdfed

Requirements
Must have
• Calm, reassuring colours. People are stressed and need to know we can help.
Should not have
• No bright oranges or yellows.

```html
<!DOCTYPE html>
<html lang="en">
<head>
<meta charset="utf-8">
<title>Velmora Clinic – Blog</title>
<link rel="stylesheet" href="https://fonts.googleapis.com/css2?family=Raleway:wght@400;500;600;700&display=swap">
<style>
:root{
  --teal:#3fb1a4;
  --teal-soft:#86cfc6;
  --sky:#cfdfed;
  --ink:#3a3a3a;
  --muted:#555;
  --dark:#3d3d3d;
  --rose:#e0443f;
}
*{box-sizing:border-box;margin:0;padding:0}
html,body{width:1200px;height:2533px;overflow:hidden}
body{font-family:"Raleway",sans-serif;color:var(--ink);background:#fff;position:relative}
a{color:inherit;text-decoration:none}

.site-header{height:103px;position:relative}
.brand{position:absolute;left:153px;top:30px;display:flex;align-items:center;gap:10px}
.brand-dot{width:36px;height:36px;border-radius:50%;background:var(--teal)}
.brand-name{font-size:26px;font-weight:500;color:var(--teal)}
.main-nav{position:absolute;left:475px;top:37px;display:flex;gap:31px;font-size:12.5px;font-weight:500;color:#444}
.main-nav a.active{position:relative}
.main-nav a.active::after{content:"";position:absolute;left:0;right:0;bottom:-14px;height:4px;background:var(--teal-soft)}
.search{position:absolute;left:934px;top:31px;width:114px;height:23px;border-radius:5px;background:#e8e8e8;font-size:11px;color:#666;padding:5px 8px}
.search svg{position:absolute;right:8px;top:6px}

.hero{position:absolute;top:103px;left:0;width:1200px;height:375px;background:var(--sky)}
.hero h1{position:absolute;left:152px;top:170px;font-size:29px;font-weight:700;color:#3d3d3d}
.hero-art{position:absolute;left:505px;top:38px;width:540px;height:337px;border-radius:200px 200px 0 0;
  background:linear-gradient(180deg,#c9b8a6 0%,#c8c4cc 45%,#4e6b5e 80%,#2e3b5a 100%)}

.post-title{position:absolute;top:520px;width:1200px;text-align:center;font-size:17px;font-weight:600}
.video{position:absolute;left:260px;top:554px;width:680px;height:416px;
  background:linear-gradient(90deg,#c7b89d 0%,#8b7a62 45%,#2d2a28 55%,#3a3633 100%)}
.video-bar{position:absolute;left:0;top:0;right:0;height:60px;background:linear-gradient(180deg,rgba(0,0,0,.55),rgba(0,0,0,0));display:flex;align-items:center;padding-left:10px;gap:10px;color:#fff;font-size:15px}
.video-bar .avatar{width:32px;height:32px;border-radius:50%;background:var(--teal);display:flex;align-items:center;justify-content:center;font-size:17px}
.video-band{position:absolute;left:0;right:0;bottom:0;height:66px;background:#e9e6e3}
.play{position:absolute;left:312px;top:188px;width:56px;height:40px;border-radius:8px;background:rgba(20,20,20,.8)}
.play::after{content:"";position:absolute;left:22px;top:12px;border-left:14px solid #fff;border-top:8px solid transparent;border-bottom:8px solid transparent}

.post-sub{position:absolute;top:990px;width:1200px;text-align:center;font-size:12.5px;font-weight:600;line-height:16px}
.post-body{position:absolute;left:152px;top:1047px;width:896px;font-size:11.5px;line-height:14.6px;color:var(--muted)}
.post-body p{margin-bottom:14.2px}
.post-body .who{color:var(--teal);font-weight:500}

.pager{position:absolute;top:2256px;left:152px;width:896px;display:flex;justify-content:space-between;font-size:13px;font-weight:700;letter-spacing:1.5px;color:#3d3d3d}
.pager span{border-bottom:3px solid var(--teal-soft);padding-bottom:2px}

.site-footer{position:absolute;top:2325px;left:0;width:1200px;height:157px;background:var(--sky)}
.foot-col{position:absolute;top:46px;font-size:13px;line-height:18px;font-weight:500;color:#3d3d3d}
.foot-call{position:absolute;left:664px;top:46px;font-size:11.5px;font-weight:600}
.foot-call span{font-weight:400}
.btn{position:absolute;left:664px;top:68px;width:230px;height:38px;border-radius:6px;background:var(--teal-soft);color:#2d5954;font-size:12px;font-weight:500;display:flex;align-items:center;justify-content:center}
.bottom-bar{position:absolute;top:2482px;left:0;width:1200px;height:51px;background:var(--dark);color:#fff;font-size:11.5px}
.bottom-bar p{position:absolute;left:152px;top:20px}
.social{position:absolute;right:152px;top:18px;display:flex;gap:8px}
.social i{width:14px;height:14px;border-radius:50%;background:#3b7bd1}
.social i:last-child{background:var(--rose)}
</style>
</head>
<body>
<header class="site-header">
  <a class="brand" href="https://www.velmoraclinic.com.au/"><span class="brand-dot"></span><span class="brand-name">Velmora Clinic</span></a>
  <nav class="main-nav">
    <a href="https://www.velmoraclinic.com.au/">Home</a>
    <a href="#">About Us</a>
    <a href="https://www.velmoraclinic.com.au/our-counselling/couples-relationship-counselling/">Relationship Counseling</a>
    <a class="active" href="https://www.velmoraclinic.com.au/blog/">Blog</a>
    <a href="https://www.velmoraclinic.com.au/contact/">Contact Us</a>
  </nav>
  <div class="search">Search
    <svg width="11" height="11" viewBox="0 0 11 11"><circle cx="4.5" cy="4.5" r="3.5" fill="none" stroke="#86cfc6" stroke-width="1.4"/><line x1="7" y1="7" x2="10" y2="10" stroke="#86cfc6" stroke-width="1.4"/></svg>
  </div>
</header>

<section class="hero">
  <h1>OUR BLOGS</h1>
  <div class="hero-art" role="img" aria-label="Flat illustration of a couple sitting close together reading a green book"></div>
</section>

<h2 class="post-title">Sexual Desires in Men and Women; What Are the Real Differences?</h2>
<div class="video" role="img" aria-label="Video thumbnail of the interview with two portrait photos">
  <div class="video-bar"><span class="avatar">T</span>Marla Quinn interviews Daniel Rourke, M.D on What Makes For Great Sex</div>
  <div class="play"></div>
  <div class="video-band"></div>
</div>
<p class="post-sub">Sexual Desires in Men and Women; What Are the Real Differences<br>Marla Quinn interviews Daniel Rourke, New York Sex Therapist and Psychiatrist – February 2020</p>

<article class="post-body">
<p><span class="who">Daniel:</span> Men’s needs are very, very simple. They want a partner who attracts them; that is to say, they like her body. She smells nice; she attracts them. You don’t hear guys saying “It’s the same thing every time.” but you hear women saying that all the time. So, I think part of the difference between Helena Voss and myself is she’s a woman and I’m a man.</p>
<p><span class="who">Marla:</span> Very interesting. Let’s talk some more about the differences between men and women. You were saying that, and I agree, most women have a fundamental need to be desired by men. Men do too, but for women, it’s more of a thing.</p>
<p><span class="who">Daniel:</span> Absolutely. It is huge. It is like oxygen for women. The most unhappy people I see are men who can’t get an erection, and women who don’t feel desired. Would you say that would fit with your practice?</p>
<p><span class="who">Marla:</span> Yes. Absolutely.</p>
<p><span class="who">Daniel:</span> Yes. A man who can’t get an erection does not feel fully like a man. And I think it might be a stretch to say that a woman who doesn’t feel desired doesn’t feel fully like a woman. But it’s close. I think it’s like oxygen. Women have to have it. And you see all sorts of mischief in a relationship if a woman doesn’t feel desired.</p>
<p><span class="who">Marla:</span> Absolutely. And you were saying in your book that you’ve had plenty of straight women who tell you that they’re going half-crazy waiting for the day that their partner will show them some real passion.</p>
<p><span class="who">Daniel:</span> Oh, my God. Yeah. And they’re furious. They’re so furious. This is what I call a sex knot. So the man doesn’t show her desire for whatever reason, and she becomes furious. And that makes him withdraw from her. And now he really doesn’t show her desire because she’s even more furious, and they could go on like this for years and never have sex. So very, very tough. Have you seen that? I’m sure.</p>
<p><span class="who">Marla:</span> Oh, absolutely. Yes. So, what’s happening here to start that off do you think? Is it that the man, once he’s caught her, feels he’s in a secure relationship? He doesn’t feel like he needs to chase her, pursue her, feel passionate towards her?</p>
<p><span class="who">Daniel:</span> It’s a good question. I think there are two things that are most often going on. The first is (and this is unfortunate about us men and it’s unfortunate for heterosexual women) that our needs are really very, very simple.</p>
<p>You know, Albrecht Kessel ask his famous question in a letter to Princess Elena Varga a hundred years ago. He said, “I’ve never been able to figure out what does a woman want?”</p>
<p>You know, nobody ever asked, “What does a man want?” Okay. Everybody knows what a man wants.</p>
<p>A man wants a nice meal and a good round of sex and then go watch the ballgame. Very, very simple. And he could do that forever. It’s like I could wear the same suit to a party forever. And I wouldn’t mind at all. We’re very, very simple. Our minds are extremely simple.</p>
<p>And women..... Women want all sorts of things. I remember when I got married, one of my senior colleagues said, “You’re not going to believe how many things your wife wants. All sorts of things.” And most women, obviously, are mature enough to know they’re not going to get everything they want. But that doesn’t stop them wanting everything.</p>
<p>And so, as I said, she wants the resort. A woman wants the beauty, they want the pleasure, they want the excitement. They want the variety. They want all these things. Half the time, the man wouldn’t even notice. A woman wants a room with a view. She wants to be able to see interesting things. Her mind is going all the time.</p>
<p>The guy is fine. You know, just let me order a hamburger and let me turn on the ballgame. It’s very, very simple with guys.</p>
<p>So, one of the reasons men stop chasing women is because they feel when they’re married to them, they feel they don’t have to. You know, they’re getting sex. It’s good. They’re fine. They’re not suffering......... but she’s suffering.</p>
<p>So that’s reason number one. Does that make sense?</p>
<p><span class="who">Marla:</span> Yes, sure.</p>
<p><span class="who">Daniel:</span> OK. I’m speaking as a man. Does it fit with your observations or am I missing something?</p>
<p><span class="who">Marla:</span> I think yes, absolutely. OK.</p>
<p><span class="who">Daniel:</span> And the second reason is that something very difficult for men happens when they settle into a committed relationship with a woman.</p>
<p>They see her unhappy at times.</p>
<p>That’s extraordinarily stressful for men because they’re not used to having intimate relationships.</p>
<p>And they don’t know that in an intimate relationship, sometimes your partner is going to be unhappy and that’s OK.</p>
<p>Women practice this. It’s a generalization, so there are exceptions. But women practice this from the age of seven. They have friends and the friend has a misunderstanding. You don’t talk to each other for a day and then you get together, you figure it out and you’re friends again. And they’re constantly maintaining relationships through the ups and downs emotionally.</p>
<p>Men don’t do that. They don’t have that kind of relationship. It’s usually not how it goes. So very often, a man’s first truly intimate relationship is with the woman that he settles in with and he sees her unhappy. And it’s very stressful for him. He doesn’t know what to do with it.</p>
<p>Let me modify that. It’s his second intimate relationship. The first intimate relationship was with his mother. And when his mother was unhappy, it was very, very stressful for him. And when he sees his partner unhappy, it gives him the same kind of stress.</p>
<p>You remember Glossmen magazine, the magazine with the centerfolds. And I hope at least some of your listeners are old enough to remember that. And the centerfold girl.... she always had this rocking hot body and beautiful makeup and hair and teeth and everything. But the real winner, the anchovy in the Caesar salad here was she had this welcoming smile. She had this big smile from ear to ear and it said, “Oh, it’s you. I’m so happy to see you. Come on in”.</p>
<p>And that’s what most guys rely on to let them know that it’s safe to come on in and it’s all right and welcome.</p>
</article>

<nav class="pager">
  <a href="#">‹ <span>PREVIOUS</span></a>
  <a href="#"><span>NEXT</span> ›</a>
</nav>

<footer class="site-footer">
  <div class="foot-col" style="left:152px">Home<br>About Us<br>Blogs<br>Contact Us</div>
  <div class="foot-col" style="left:360px">Relationship Counseling<br>Sex Therapy<br>Fees and Rebates<br>FAQ’s</div>
  <p class="foot-call">Call Us Now <span>1300 555 014</span></p>
  <a class="btn" href="https://www.velmoraclinic.com.au/contact/">REQUEST AN APPOINTMENT</a>
</footer>
<div class="bottom-bar">
  <p>© 2020 Velmora Clinic. All rights reserved.</p>
  <div class="social"><i></i><i></i><i></i><i></i></div>
</div>
</body>
</html>
```